Sponsorship and registration document for Charity Golf Day 2022

The project requires 2 documents to be updated to look more graphically savvy and professionally presentable.
1. Charity golf day sponsorship document
2. One page registration document.
The text has been completed. Text not to be changed - just graphics.
New images would be preferred.
The logos have been provided.

Target Market(s)

Corporate Sponsors and Golf players

Requirements
Must have
• Golf Theme

```html
<!DOCTYPE html>
<html lang="en">
<head>
<meta charset="utf-8">
<title>Charity Golf Day 2022 – Sponsorship Proposal &amp; Registration</title>
<link href="https://fonts.googleapis.com/css2?family=Montserrat:wght@600;700;800&family=Open+Sans:ital,wght@0,400;0,600;0,700;1,400&family=Lora:ital,wght@0,400;1,400;1,700&display=swap" rel="stylesheet">
<style>
:root{
  --green:#4f8a2e;
  --green-deep:#3d6e25;
  --green-text:#3f7a22;
  --pale:#c6e3b1;
  --pale-soft:#e6f2dc;
  --band:#a8d388;
  --gold:#f2c21b;
  --ink:#4a4a4a;
  --rule:#c9d9be;
}
*{margin:0;padding:0;box-sizing:border-box}
html,body{width:1200px;height:618px;overflow:hidden;background:#fff}
.sheet{position:relative;width:1200px;height:618px;background:#fff}
.page{position:absolute;width:223px;height:288px;background:#fff;overflow:hidden;box-shadow:0 0 0 .6px #d4d4d4;font:3.5px/1.38 'Open Sans',sans-serif;color:var(--ink)}
.photo{background:linear-gradient(180deg,#d5e6ef 0%,#b9d3c0 38%,#7fb04a 62%,#4d8524 82%,#36651a 100%)}
.hdr{position:absolute;top:0;left:0;right:0;height:27.5px;display:flex}
.hdr .photo{width:68px}
.hdr .title{width:65px;background:var(--green);color:#fff;font:800 5.1px/1.05 'Montserrat',sans-serif;display:flex;align-items:center;justify-content:center;text-align:center}
.hdr .tag{flex:1;background:var(--pale);color:#3e6a26;font:italic 6.6px/1 'Lora',serif;display:flex;align-items:center;justify-content:center}
.foot{position:absolute;left:0;right:0;bottom:0;height:9.5px;background:var(--band)}
.ball{position:absolute;right:17px;bottom:10px;width:13px;height:17px}
.body{position:absolute;top:40px;left:19.5px;right:19.5px}
h2{font:700 5.1px/1.3 'Open Sans',sans-serif;color:var(--green-text);margin-bottom:3px}
h3{font:700 4.6px/1.3 'Open Sans',sans-serif;color:var(--green-text);margin:4px 0 2px}
p{margin-bottom:3px}
ul{padding-left:6px;margin-bottom:3px}
ul.sq{list-style:square}
li{margin-bottom:.3px}
a,.link{color:var(--green-text);text-decoration:none}
b{font-weight:700;color:#333}

/* cover */
.cover .hero{position:absolute;top:0;left:0;right:0;height:129px}
.cover .band{position:absolute;top:129px;left:0;right:0;height:65px;background:var(--green-deep);text-align:center;color:#fff}
.cover .band h1{font:800 15.5px/1 'Montserrat',sans-serif;margin-top:5px;letter-spacing:.2px}
.cover .band .date{font:400 8px/1 'Open Sans',sans-serif;margin-top:6px}
.cover .band .venue{font:800 9.4px/1 'Montserrat',sans-serif;color:var(--gold);margin-top:4px}
.cover .band .web{font:600 6.6px/1 'Open Sans',sans-serif;margin-top:4px}
.cover .side{position:absolute;top:194px;left:0;width:110px;bottom:0;background:var(--pale);text-align:center;color:#2f3a2a}
.cover .side .kind{font:600 8.3px/1.25 'Open Sans',sans-serif;margin-top:13px}
.cover .side .dot{width:3px;height:3px;border-radius:50%;background:#2f3a2a;margin:7px auto 0}
.cover .side .cause{font:400 8.4px/1.35 'Lora',serif;margin-top:7px}
.cover .slogan{position:absolute;top:194px;left:110px;right:0;height:45px;background:var(--green);color:#fff;font:italic 700 5.6px/1.45 'Lora',serif;text-align:center;padding-top:6px}
.cover .org{position:absolute;top:252px;left:120px;display:flex;align-items:center;gap:5px}
.org-name{font:600 6.6px/1.1 'Open Sans',sans-serif;color:var(--green-deep);text-align:right}
.org-mark{width:12px;height:12px;background:var(--pale)}

/* contents */
.toc{width:100%;border-collapse:collapse;margin-bottom:20px}
.toc td{height:10.4px;padding:0 2px;border-top:.4px solid var(--rule)}
.toc tr:nth-child(even) td{background:var(--pale-soft)}
.toc td.num{text-align:right;padding-right:8px}
.contact p{margin-bottom:0}
.contact .name{font-weight:700;color:var(--green-text)}
.sig{width:38px;height:10px;background:linear-gradient(90deg,#eef2f8,#dfe6f1);margin:3px 0 4px}

/* schedule */
.sched{display:grid;grid-template-columns:50px 13px 1fr;margin-top:1px}
.center{text-align:center}

/* forms */
.ticks{display:flex;gap:3px;align-items:center;font-weight:700;color:var(--green-text);margin:6px 0 4px;white-space:nowrap}
.box{display:inline-block;width:4px;height:4px;border:.5px solid #555;vertical-align:middle;margin-right:1.5px}
.noBox{margin-left:auto;width:43px;height:8.5px;border:.5px solid #777;padding-left:3px;display:flex;align-items:center;margin-bottom:7px}
.field{display:flex;align-items:flex-end;height:9.3px;white-space:nowrap}
.field .lbl{width:36px;flex:none}
.field .line{flex:1;border-bottom:.5px dotted #777;height:2px}
.note{font-style:italic;color:#7a9b65;margin-top:3px}
.pay{display:grid;grid-template-columns:30px 1fr;row-gap:.6px}
.pay .k{color:var(--green-text)}
.cardrow{display:flex;align-items:center;white-space:nowrap}

/* registration page */
.reg .top{position:absolute;top:0;left:0;right:0;height:27.5px;display:flex}
.reg .top .photo{width:82px}
.reg .top .banner{flex:1;background:var(--green);color:#fff;text-align:center}
.reg .top .banner .t{font:800 9.3px/1 'Montserrat',sans-serif;margin-top:7px}
.reg .top .banner .s{font:600 5px/1 'Open Sans',sans-serif;color:var(--gold);margin-top:2px}
.reg .strip{position:absolute;top:27.5px;left:0;right:0;height:8px;background:var(--pale-soft);display:flex;align-items:center;justify-content:center;gap:5px;font-size:3.2px;color:#333}
.reg .strip span{display:flex;align-items:center;gap:1.5px}
.pin{width:3.4px;height:3.4px;border-radius:50%;background:var(--green)}
.rbox{position:absolute;background:var(--pale-soft);border:.4px solid #b9cfa9;padding:2px;font-size:3.4px;line-height:1.35;text-align:justify}
.rbox.white{background:#fff}
.rbox .hd{font-weight:700;color:#333}
.grid2{display:grid;grid-template-columns:26px 1fr;font-size:3.2px;line-height:1.3}
.regform{position:absolute;top:124px;left:13px;right:14px}
.regform h4{font:700 5.2px/1.2 'Open Sans',sans-serif;color:#2e3a2a}
.regform .field{height:7.6px}
.regform .field .lbl{width:26px}
.rtable{width:100%;border-collapse:collapse;margin-top:3px;font-size:3.2px}
.rtable th{font-weight:400;border:.4px solid #c8c8c8;height:8px;line-height:1.1}
.rtable td{border:.4px solid #c8c8c8;height:5px;padding-left:1.5px}
.fine{position:absolute;left:13px;top:241px;width:147px;height:34px;background:var(--pale);padding:2.5px 3px;font-size:2.6px;line-height:1.35;color:#3a3a3a}
.reg .org{position:absolute;right:14px;top:254px;display:flex;align-items:center;gap:3px}
.reg .org .org-name{font-size:4.4px}
.reg .org .org-mark{width:8px;height:8px}
</style>
</head>
<body>
<main class="sheet">

<svg width="0" height="0" style="position:absolute">
  <defs>
    <symbol id="tee-ball" viewBox="0 0 13 17">
      <circle cx="6.5" cy="6" r="5.5" fill="#fff" stroke="#9a9a9a" stroke-width=".6"/>
      <path d="M3.5 11.6h6l-2 1.6v3.2h-2v-3.2z" fill="#c9c9c9"/>
      <ellipse cx="6.5" cy="16.4" rx="5" ry=".8" fill="#7fb04a"/>
    </symbol>
  </defs>
</svg>

<!-- Page 1: cover -->
<section class="page cover" style="left:18.6px;top:18.6px">
  <div class="hero photo" role="img" aria-label="Photo of a golf ball on a tee in green grass with a club head behind it"></div>
  <div class="band">
    <h1>CHARITY GOLF DAY</h1>
    <div class="date">Friday 25 March 2022</div>
    <div class="venue">Elmwood Golf Club</div>
    <div class="web">www.rsc.org.au/golf-day</div>
  </div>
  <div class="side">
    <div class="kind">SPONSORSHIP<br>PROPOSAL</div>
    <div class="dot"></div>
    <div class="cause">Supporting Prostate<br>Cancer Research</div>
  </div>
  <div class="slogan">Help us hit prostate cancer<br>off the green and beat<br>the most common cancer in<br>Australian Men.</div>
  <div class="org"><div class="org-name">Riverside<br>Service Club</div><div class="org-mark"></div></div>
</section>

<!-- Page 2: contents -->
<section class="page" style="left:253px;top:18.6px">
  <header class="hdr"><div class="photo" role="img" aria-label="Golf ball on tee photo"></div><div class="title">CHARITY<br>GOLF DAY</div><div class="tag">Sponsorship Proposal</div></header>
  <div class="body" style="top:48px">
    <h2>Contents</h2>
    <table class="toc">
      <tr><td>Charity Golf Day Invitation</td><td class="num">2</td></tr>
      <tr><td>About Prostate Cancer</td><td class="num">3</td></tr>
      <tr><td>Why are we asking you to be involved</td><td class="num">3</td></tr>
      <tr><td>What to expect</td><td class="num">4</td></tr>
      <tr><td>Sponsorship Opportunities</td><td class="num">5</td></tr>
      <tr><td>Application Form</td><td class="num">7</td></tr>
    </table>
    <div class="contact">
      <h2 style="margin-bottom:1px">Contact</h2>
      <p class="name">Mara (Kostas) Whitfield</p>
      <p>Convenor</p>
      <p>Co - President, Riverside Service Club</p>
      <p><b>Mobile</b> : 0400 555 218</p>
      <p><b>Email</b> : mara.whitfield@mailbox.com</p>
      <p><b>Web</b> : www.rsc.org.au/golf-day</p>
      <p class="name" style="margin-top:13px">Livia Marchetti</p>
      <p>Event Manager</p>
      <p>Email : livia.marchetti@netmail.com</p>
    </div>
  </div>
  <svg class="ball"><use href="#tee-ball"/></svg>
  <div class="foot"></div>
</section>

<!-- Page 3: invitation letter -->
<section class="page" style="left:486.8px;top:18.6px">
  <header class="hdr"><div class="photo" role="img" aria-label="Golf ball on tee photo"></div><div class="title">CHARITY<br>GOLF DAY</div><div class="tag">Sponsorship Proposal</div></header>
  <div class="body" style="top:42px;text-align:justify">
    <h2 style="font-size:5px;line-height:1.5;margin-bottom:4px">Join us for an exclusive day on the private Elmwood Golf Course, with all proceeds going to support Prostate Cancer Research, Awareness and Support.</h2>
    <p>The Riverside Service Club will again be holding its Charity Golf Day with all proceeds used to support the Prostate Cancer Research, awareness and Support Programs. The venue will be the prestigious Elmwood Golf Club on Friday 25 March 2022, with a shotgun start at 8:00 am.</p>
    <p>We have enclosed for your information a copy of our promotional sponsor packages that outline the event, sponsorship package options and inclusions.</p>
    <p>The format of the day involves:</p>
    <ul>
      <li>Player registration, refreshments and light breakfast from 7:00am</li>
      <li>Ambrose competition starting at 8:00am</li>
      <li>Two Course lunch and presentations in the club house from 12:30pm</li>
    </ul>
    <p>Your commitment to supporting health programs in our community is truly appreciated. With assistance from sponsors such as yourself, we will continue to see improvements in the support and treatment for men and their families with prostate cancer.</p>
    <p>We hope that you will consider supporting the worthwhile event that is open to any organisation or individual who wishes to enjoy the benefits of playing golf at the prestigious Elmwood Golf Club.</p>
    <p>For more information, please check the website (www.rsc.org.au/golf-day) or should you wish to discuss any aspect of the event, please contact me on 0400 555 218.</p>
    <p>Yours sincerely</p>
    <div class="sig" role="img" aria-label="Handwritten signature"></div>
    <p style="margin:0"><b>Mara (Kostas) Whitfield</b><br><b>Convener</b><br>Co- President 2021 -2022<br>Secretary 2021 - 2022<br>Riverside Service Club</p>
  </div>
  <svg class="ball"><use href="#tee-ball"/></svg>
  <div class="foot"></div>
</section>

<!-- Page 4: about prostate cancer -->
<section class="page" style="left:720.6px;top:18.6px">
  <header class="hdr"><div class="photo" role="img" aria-label="Golf ball on tee photo"></div><div class="title">CHARITY<br>GOLF DAY</div><div class="tag">Sponsorship Proposal</div></header>
  <div class="body" style="top:42px;text-align:justify">
    <h2>Why prostate cancer?</h2>
    <ul>
      <li>Prostate cancer is the most diagnosed cancer in Australian men.</li>
      <li>Approximately 20,000 Australian men are diagnosed with prostate cancer each year.</li>
      <li>Over 200,000 Australian men are living with a diagnosis prostate cancer.</li>
      <li>95% of Australian men diagnosed with prostate cancer survive for at least 5 years.</li>
      <li>Almost 3,500 Australian men die of prostate cancer each year.</li>
    </ul>
    <h2 style="margin-top:5px">Why are we asking you to be involved?</h2>
    <ul>
      <li>Every day 54 Australian men will be told they have prostate cancer</li>
      <li>70% of research applications are unfunded</li>
      <li>1 in 6 men will suffer from prostate cancer</li>
      <li>9 families lose a loved one to prostate cancer every day</li>
      <li>Only 1 in 3 men have access to a specialist nurse</li>
    </ul>
    <h2 style="margin-top:5px">What this fundraising event can achieve</h2>
    <ul>
      <li><b>$ 12,500 –</b> Could provide funding for a researcher working for one month on a project to reduce side – effects post treatment.</li>
      <li><b>$ 30,000 –</b> could provide finding for a senior scientist for three months working on a project to improve treatments for prostate cancer that has spread to the bones.</li>
      <li><b>$ 50,000 –</b> could fund a project to improve early – diagnosis for men with a family history of prostate cancer.</li>
    </ul>
    <p>Proceeds from this event will be donated to Prostate Cancer Research Group at the Eastvale University Discovery Institute, to fund world leading, innovative research and to support men and their families affected by prostate cancer.</p>
    <p>Their innovative research program has a strong translational approach, involving lab-based studies with tissues donated by patients with prostate cancer. Their collaborative studies with clinicians and patient advocates address questions that are relevant to patient care. The findings have the potential to improve the management and outcomes of men with different stages of prostate cancer. Recent studies have informed international guidelines for diagnosis of prostate cancer and led to new clinical trials. For more information visit their website <span class="link">www.eastvale.edu/discovery/prostate-research</span></p>
  </div>
  <svg class="ball"><use href="#tee-ball"/></svg>
  <div class="foot"></div>
</section>

<!-- Page 5: what to expect -->
<section class="page" style="left:955px;top:18.6px">
  <header class="hdr"><div class="photo" role="img" aria-label="Golf ball on tee photo"></div><div class="title">CHARITY<br>GOLF DAY</div><div class="tag">Sponsorship Proposal</div></header>
  <div class="body" style="top:44px">
    <h2 class="center" style="font-size:5.6px">Friday 25 March 2022 at Elmwood Golf Club</h2>
    <p>The Championship Par 72 layout of 6179 metres is a genuine test to all standards of players. Situated only 15 minutes from the city, the course meanders along the Yarra River providing a beautiful vista and is home for 100's of species of native birds and tall-established trees.</p>
    <h3>Breakfast</h3>
    <ul class="sq"><li>Light Breakfast</li><li>Tea and coffee</li></ul>
    <h3>Lunch</h3>
    <ul class="sq"><li>Two-Course Lunch</li><li>Drinks at Bar Prices</li></ul>
    <h3>What else to expect</h3>
    <ul class="sq">
      <li>4-person Ambrose</li>
      <li>On course competitions such as nearest the pins and longest drive</li>
      <li>Trophies &amp; Prizes</li>
      <li>On the day you will have access to practice putting, chipping greens, and driving range</li>
      <li>A refreshment cart will circulate the golf course for players to purchase refreshments at own cost</li>
      <li>Hire Equipment
        <ul style="list-style:circle;margin:0">
          <li>Hire sets (Standard) $35.00 per set; (Premium) $50.00 per set</li>
          <li>Hire shoes $10.00 per pair</li>
          <li>Carts $40.00 each (Booking essential as numbers are limited, but it is an easy course to walk)</li>
        </ul>
      </li>
    </ul>
    <h3>Schedule</h3>
    <div class="sched">
      <span>07:00 am to 07:30 am</span><span>:</span><span>Registration</span>
      <span>07:15 am</span><span>:</span><span>Breakfast</span>
      <span>07:45 am</span><span>:</span><span>Player Briefing</span>
      <span>08:00 am</span><span>:</span><span>Shotgun start</span>
      <span>12.30 pm</span><span>:</span><span>Lunch, Presentation/Prizes</span>
      <span>03.00 pm</span><span>:</span><span>Finish</span>
    </div>
  </div>
  <svg class="ball"><use href="#tee-ball"/></svg>
  <div class="foot"></div>
</section>

<!-- Page 6: gold & silver -->
<section class="page" style="left:18.6px;top:315.4px">
  <header class="hdr"><div class="photo" role="img" aria-label="Golf ball on tee photo"></div><div class="title">CHARITY<br>GOLF DAY</div><div class="tag">Sponsorship Proposal</div></header>
  <div class="body" style="top:48px">
    <h2 class="center" style="font-size:5.6px">Sponsorship Opportunities</h2>
    <h3 style="font-size:5px">Gold $5,000</h3>
    <p>The Gold Sponsor is entitled to the following:</p>
    <ul class="sq">
      <li>Event naming rights</li>
      <li>Eight (8) representatives playing in the event, including all green fees, four (4) carts, light breakfast &amp; 2 course lunch</li>
      <li>Your company signage / banners displayed exclusively at club entrance and social area.</li>
      <li>Your logo and your company information on all promotional and marketing material being used on the day including our website, email to database and our social media channels.</li>
      <li>A Banner with company logo on the first hole</li>
      <li>Opportunity to say a few words at the beginning of the game as the chief sponsor of the event.</li>
      <li>Your company merchandise on display.</li>
      <li>Presenting the winners awards</li>
      <li>Free advertising in our Service Club Newsletter, website, and social media channels for 12 months.</li>
      <li>Opportunity to “capture” prospective clients on the day</li>
      <li>Great Publicity: Be seen as being associated with an excellent cause</li>
    </ul>
    <h3 style="font-size:5px">Silver $2,500</h3>
    <p>The Silver Sponsor is entitled to the following:</p>
    <ul class="sq">
      <li>Four (4) representatives playing in the event, including all green fees, two (2) carts, light breakfast &amp; 2 course lunch</li>
      <li>Exclusive banner with your company logo on a tee of choice (except hole 1)</li>
      <li>Opportunity to say a few words as a major sponsor</li>
      <li>Your company merchandise on display.</li>
      <li>Your logo and your company information on all promotional and marketing material being used on the day including our website, email to database and our social media channels.</li>
      <li>Free advertising in our Service Club Newsletter, website, and social media channels for 6 months.</li>
      <li>Opportunity to “capture” prospective clients on the day</li>
      <li>Great Publicity: Be seen as being associated with an excellent cause</li>
    </ul>
  </div>
  <svg class="ball"><use href="#tee-ball"/></svg>
  <div class="foot"></div>
</section>

<!-- Page 7: bronze & payment -->
<section class="page" style="left:253px;top:315.4px">
  <header class="hdr"><div class="photo" role="img" aria-label="Golf ball on tee photo"></div><div class="title">CHARITY<br>GOLF DAY</div><div class="tag">Sponsorship Proposal</div></header>
  <div class="body" style="top:46px">
    <h2>Bronze $650</h2>
    <p>This Bronze Sponsor is entitled to the following:</p>
    <ul style="padding-left:13px">
      <li>Two (2) representatives playing in the event, including all green fees, light breakfast &amp; 2 course lunch</li>
      <li>Exclusive banner with your company logo on a tee</li>
      <li>Your logo and your company information on all promotional and marketing material being used on the day including our website, email to database and our social media channels.</li>
      <li>Great Publicity: Be seen as being associated with an excellent cause</li>
      <li>Opportunity to “capture” prospective clients on the day</li>
      <li>Company merchandising display</li>
      <li>Additional players - $150 per person (including all green fees, light breakfast &amp; 2-course lunch).</li>
    </ul>
    <p style="margin-top:10px"><span style="font:700 5px 'Open Sans',sans-serif;color:var(--green-text)">Additional Players - $150 per person –</span> includes all green fees, light breakfast &amp; two (2) course lunch</p>
    <h2 style="margin-top:11px;margin-bottom:1px">PAYMENT OPTIONS</h2>
    <div class="pay">
      <span class="k">By Cheque :</span><span>Please make cheques payable to <span class="link">The Riverside Service Club</span><br>PO Box 42<br>Hillcrest East, Vic 3100</span>
      <span class="k">By Direct Deposit:</span><span><span class="k">Account Name :</span> Riverside Service Club<br><span class="k">Bank :</span> Valley Bank<br><span class="k">BSB :</span> 071 204<br><span class="k">Account Number :</span> 302 118 946<br><span class="k">Comment :</span> RSCGolfDay/your name</span>
      <span class="k" style="white-space:nowrap">By Credit Card :</span><span class="cardrow"><span class="k" style="margin-left:4px">NovaCard</span>&nbsp;<span class="box"></span><span class="k" style="margin-left:14px">OrbitCard</span>&nbsp;<span class="box"></span></span>
      <span></span><span style="display:flex;justify-content:space-between;margin-top:2px;white-space:nowrap">Card No. ____ ____ ____ ____<span>Expiry __ / __</span></span>
      <span></span><span class="field" style="height:6.5px"><span class="lbl" style="width:auto;margin-right:2px">Cardholder's Name:</span><span class="line"></span></span>
      <span></span><span class="field" style="height:6.5px"><span class="lbl" style="width:auto;margin-right:2px">Cardholder's Signature:</span><span class="line"></span><span style="margin:0 2px">Date:</span><span class="line" style="flex:.45"></span></span>
    </div>
  </div>
  <svg class="ball"><use href="#tee-ball"/></svg>
  <div class="foot"></div>
</section>

<!-- Page 8: application form -->
<section class="page" style="left:486.8px;top:315.4px">
  <header class="hdr"><div class="photo" role="img" aria-label="Golf ball on tee photo"></div><div class="title">CHARITY<br>GOLF DAY</div><div class="tag">Application Form</div></header>
  <div class="body" style="top:44px">
    <h2>Sponsorship Package: (Please Tick)</h2>
    <div class="ticks"><span><span class="box"></span>Gold ($5,000)</span><span><span class="box"></span>Silver ($2,500)</span><span><span class="box"></span>Bronze ($650)</span><span><span class="box"></span>Additional Players ($150)</span></div>
    <div class="noBox">No. :</div>
    <div class="field"><span class="lbl">Company</span><span class="line"></span></div>
    <div class="field"><span class="lbl">Address</span><span class="line"></span></div>
    <div class="field"><span class="lbl">Suburb</span><span class="line"></span><span style="margin:0 1px 0 3px">P/Code:</span><span class="line" style="flex:.5"></span></div>
    <div class="field"><span class="lbl">Mobile</span><span class="line"></span></div>
    <div class="field"><span class="lbl">Contact Name</span><span class="line"></span></div>
    <div class="field"><span class="lbl">Contact Email</span><span class="line"></span></div>
    <h2 style="margin-top:10px;margin-bottom:0">Team Name</h2>
    <div class="field"><span class="lbl">Player 1</span><span class="line"></span></div>
    <div class="field"><span class="lbl">Official GA H/Cap</span><span class="line" style="flex:.32"></span><span style="flex:.68"></span></div>
    <div class="field"><span class="lbl">Player 2</span><span class="line"></span></div>
    <div class="field"><span class="lbl">Official GA H/Cap</span><span class="line" style="flex:.32"></span><span style="flex:.68"></span></div>
    <div class="field"><span class="lbl">Player 3</span><span class="line"></span></div>
    <div class="field"><span class="lbl">Official GA H/Cap</span><span class="line" style="flex:.32"></span><span style="flex:.68"></span></div>
    <div class="field"><span class="lbl">Player 4</span><span class="line"></span></div>
    <div class="field"><span class="lbl">Official GA H/Cap</span><span class="line" style="flex:.32"></span><span style="flex:.68"></span></div>
    <p class="note">Please Note: Any player without an official GA H/Cap will be given a maximum handicap of 27 (Males) &amp; 36 (Females).</p>
  </div>
  <svg class="ball"><use href="#tee-ball"/></svg>
  <div class="foot"></div>
</section>

<!-- Page 9: team & cancellation -->
<section class="page" style="left:720.6px;top:315.4px">
  <header class="hdr"><div class="photo" role="img" aria-label="Golf ball on tee photo"></div><div class="title">CHARITY<br>GOLF DAY</div><div class="tag">Application Form</div></header>
  <div class="body" style="top:46px">
    <h2 style="margin-bottom:0">Team Name</h2>
    <div class="field"><span class="lbl">Player 5</span><span class="line"></span></div>
    <div class="field"><span class="lbl">Official GA H/Cap</span><span class="line"></span></div>
    <div class="field"><span class="lbl">Player 6</span><span class="line"></span></div>
    <div class="field"><span class="lbl">Official GA H/Cap</span><span class="line"></span></div>
    <div class="field"><span class="lbl">Player 7</span><span class="line"></span></div>
    <div class="field"><span class="lbl">Official GA H/Cap</span><span class="line"></span></div>
    <div class="field"><span class="lbl">Player 8</span><span class="line"></span></div>
    <div class="field"><span class="lbl">Official GA H/Cap</span><span class="line"></span></div>
    <p class="note">Please Note: Any player without an official GA H/Cap will be given a maximum handicap of 27 (Males) &amp; 36 (Females).</p>
    <h2 style="margin-top:9px;color:#2f3a2a">Cancellation Terms</h2>
    <p style="text-align:justify">If the organiser cancels the event prior to the scheduled date, the sponsor is entitled to a 100% refund. If the event is rescheduled by the organiser, and the player or sponsor can reasonably demonstrate their inability to participate they will be entitled to a full refund. In the event of a player or sponsor cancellation, the Riverside Service Club reserves the right to retain monies paid in full unless resold. Any cancellations must be advised in writing via email to the Convenor Mara Whitfield (mara.whitfield@mailbox.com).</p>
  </div>
  <svg class="ball"><use href="#tee-ball"/></svg>
  <div class="foot"></div>
</section>

<!-- Page 10: one-page registration -->
<section class="page reg" style="left:955px;top:315.4px">
  <header class="top">
    <div class="photo" role="img" aria-label="Golf ball on tee photo"></div>
    <div class="banner"><div class="t">2022 CHARITY GOLF DAY</div><div class="s">Friday 25 March 2022 | Elmwood Golf Club</div></div>
  </header>
  <div class="strip"><span><i class="pin"></i>88 Linden Road, East Elmwood</span><span><i class="pin"></i>www.rsc.org.au/golf-day</span></div>

  <div class="rbox" style="left:13px;top:45px;width:56px;height:19px">Do you care about prostate cancer and fighting this disease ?</div>
  <div class="rbox white" style="left:13px;top:67px;width:56px;height:24px;color:#222">Help us hit prostate cancer off the green and beat the most common cancer in Australian men.</div>
  <div class="rbox" style="left:13px;top:96px;width:56px;height:20px">Enter a team or as an individual in the 2022 Charity Golf Day.</div>
  <div class="rbox white" style="left:74px;top:45px;width:48px;height:76px;color:#666">Proceeds from this event will be donated to Prostate Cancer Research Group at the Eastvale University Discovery Institute, to fund world leading, innovative research and to support men and their families affected by prostate cancer.</div>
  <div class="rbox" style="left:127px;top:45px;width:82px;height:30px;text-align:left"><span class="hd">COST INFORMATION:</span><br><span class="hd">$ 150 per player</span><br>Cost includes golf, light breakfast with coffee/tea on arrival and a two- course lunch following the game.</div>
  <div class="rbox white" style="left:127px;top:78px;width:82px;height:44px;text-align:left">
    <span class="hd">EVENT INFORMATION</span>
    <div class="grid2"><b>Event</b><b>4 person Ambrose</b><span>07:00 am</span><span>Registration</span><span>07:15 am</span><span>Breakfast</span><span>07:45 am</span><span>Briefing</span><span>08:00 am</span><span>Shotgun start</span><span>12.30 pm</span><span>Lunch</span><span>02.00 pm</span><span>Presentation/Prizes</span><span>03.00 pm</span><span>Finish</span></div>
  </div>

  <div class="regform">
    <h4>REGISTRATION FORM</h4>
    <p style="margin:0;font-size:3.4px;color:#222">Please complete the details below and return via e-mail<br>to : mara.whitfield@mailbox.com</p>
    <div class="field"><span class="lbl">Name</span><span class="line"></span></div>
    <div class="field"><span class="lbl">Organisation</span><span class="line"></span></div>
    <div class="field"><span class="lbl">Address</span><span class="line"></span></div>
    <div class="field"><span class="lbl">Mobile</span><span class="line"></span><span style="margin:0 1px 0 2px">Email:</span><span class="line"></span></div>
    <table class="rtable">
      <tr><th style="width:28%">NAME OF PLAYERS</th><th style="width:30%">EMAIL</th><th>MOBILE</th><th style="width:8%">GA H'CAP</th><th style="width:13%">GOLF ID NO.</th></tr>
      <tr><td>1.</td><td></td><td></td><td></td><td></td></tr>
      <tr><td>2.</td><td></td><td></td><td></td><td></td></tr>
      <tr><td>3.</td><td></td><td></td><td></td><td></td></tr>
      <tr><td>4.</td><td></td><td></td><td></td><td></td></tr>
    </table>
    <p style="font-size:3.1px;margin:1px 0 2px"><b><i>Please Note:</i></b> <i>Players without an official GA Handicap will be given a maximum handicap of 27 (Men) and 36 (Ladies)</i></p>
    <p style="display:flex;justify-content:space-between;margin-bottom:1px;color:#222"><b>COST: <span style="font-weight:400">$150 per player</span></b><b>TOTAL : $ ..................</b></p>
    <p style="margin-bottom:0"><b>METHOD OF PAYMENT (Please tick):</b></p>
    <div style="display:grid;grid-template-columns:1.7fr .55fr 1fr;font-size:3px;line-height:1.3">
      <span><span class="box" style="width:2.6px;height:2.6px"></span><i>Cheque payable to Riverside Service Club</i><br>Form and cheque can be mailed to Mara Kostas,<br>c/- PO Box 42, Hillcrest East Vic 3100</span>
      <span><span class="box" style="width:2.6px;height:2.6px"></span>EFT<br>BSB: 071 204<br>Comment :</span>
      <span><br>Account No: 302 118 946<br>RSCGolf and your surname</span>
    </div>
  </div>

  <div class="fine">CANCELLATIONS: Fees are non-refundable or transferable. Substitutions can be made in writing addressed to Mara via email to mara.whitfield@mailbox.com. RSC will only reimburse registration fees if the event is cancelled. RSC is not responsible for any costs incurred as a result. Non-attendance: if a player fails to attend, fees will not be refunded or allocated to another event.</div>
  <div class="org"><div class="org-name">Riverside<br>Service Club</div><div class="org-mark"></div></div>
  <div class="foot" style="height:6px"></div>
</section>

</main>
</body>
</html>
```